Awesome Professional Template for a collaborative report

File format: A4 PDF ideally

Design Requirements:

3 or 4 variants of a template some with graphics and pull quotes and a bio page for the essayists with a profile pic and a short descriptor

Layout Format: PPT would be perfect ideally portrait format

Style/Reference Guide: Varnholt or QP styles thought leadership reports as a guide

We need to input 10 essays around a specific subject with a nice layout with place holders for high impact pull quotes from the copy, stunning colourway and typrography probably A4 format but emailed as a PDF ideally not a huge file size. Striking front cover with title and list of contributors plus layout variations for the essays which will include a head shot short profile and contacts for the authors. Ideally a portrait format PPT that is easy to work with.

Target Market(s)

business professionals in brands

Industry/Entity Type

brand marketing

Font styles to use
Sans Serif

Colors
0054AA
0677BA
7BADD7
CADEEF
E8F1F8
00AB8E
00BBA5
67D7C9
C6EFE9
E9F9F6
F0912C
F2A743
F7CA91
FBE8D2
FDF5EE
6B429C
8869AF
B7A5CE
E3DAEB
F3F0F8

Requirements
Must have
• awesome visual impact

```html
<!DOCTYPE html>
<html lang="en">
<head>
<meta charset="utf-8">
<title>The Truth About New AI — Cover</title>
<link rel="stylesheet" href="https://fonts.googleapis.com/css2?family=IBM+Plex+Sans:wght@300;400;500;700&display=swap">
<style>
  :root {
    --ink: #181b22;
    --white: #ffffff;
    --cyan: #4fc3d9;
    --purple: #4b2a7b;
    --navy: #061634;
    --art-light: #f4f5f6;
    --art-mid: #c9cdd1;
  }
  html, body {
    margin: 0;
    padding: 0;
    overflow: hidden;
    background: var(--ink);
  }
  .cover {
    position: relative;
    width: 845px;
    height: 1200px;
    overflow: hidden;
    background: var(--ink);
    font-family: "IBM Plex Sans", Arial, sans-serif;
    color: var(--white);
  }
  .cover-graphic {
    position: absolute;
    left: 0;
    top: 0;
    width: 845px;
    height: 1200px;
  }
  .kicker {
    position: absolute;
    left: 77px;
    top: 92px;
    margin: 0;
    font-size: 19px;
    font-weight: 500;
    letter-spacing: 0.1px;
  }
  .issue-date {
    position: absolute;
    left: 749px;
    top: 96px;
    width: 68px;
    height: 16px;
    margin: 0;
    font-size: 14px;
    font-weight: 400;
    letter-spacing: 1px;
    line-height: 16px;
    transform-origin: 0 0;
    transform: translate(0, 68px) rotate(-90deg);
  }
  .title {
    position: absolute;
    right: 75px;
    top: 504px;
    margin: 0;
    text-align: right;
    font-weight: 400;
  }
  .title-lead {
    display: block;
    font-size: 42px;
    font-weight: 400;
    line-height: 60px;
    letter-spacing: 0.3px;
  }
  .title-main {
    display: block;
    font-size: 92px;
    font-weight: 700;
    line-height: 86px;
    letter-spacing: 1px;
    margin-right: -3px;
  }
  .summary {
    position: absolute;
    right: 104px;
    top: 1090px;
    margin: 0;
    text-align: right;
    font-size: 14.5px;
    line-height: 18px;
    font-weight: 400;
  }
  .summary-bar {
    position: absolute;
    left: 757px;
    top: 1077px;
    width: 8px;
    height: 65px;
    background: var(--cyan);
  }
</style>
</head>
<body>
  <main class="cover">
    <svg class="cover-graphic" viewBox="0 0 845 1200" aria-hidden="false">
      <defs>
        <radialGradient id="artTone" cx="0.4" cy="0.45" r="0.6">
          <stop offset="0" stop-color="var(--art-mid)"/>
          <stop offset="1" stop-color="var(--art-light)"/>
        </radialGradient>
        <clipPath id="discClip">
          <circle cx="466" cy="605" r="379"/>
        </clipPath>
      </defs>

      <circle class="art-disc" cx="466" cy="605" r="379" fill="url(#artTone)"
              role="img" aria-label="Illustration of a low-poly wireframe human head made of connected nodes and lines"/>

      <path class="accent-arc" d="M 228 302 A 390 390 0 0 0 205 893"
            fill="none" stroke="var(--cyan)" stroke-width="8"/>

      <circle class="purple-sweep" cx="866" cy="603" r="525" fill="var(--purple)" clip-path="url(#discClip)"/>
      <circle class="purple-ring" cx="846" cy="596" r="343" fill="var(--purple)"/>
      <circle class="navy-disc" cx="846" cy="596" r="332" fill="var(--navy)"/>
    </svg>

    <p class="kicker">a collaborative project</p>
    <p class="issue-date">JUL 2023</p>

    <h1 class="title">
      <span class="title-lead">The Truth About</span>
      <span class="title-main">NEW AI</span>
    </h1>

    <p class="summary">15 expert essays about the {add adjective} nature of<br>current AI tech, by leading industry experts.</p>
    <div class="summary-bar"></div>
  </main>
</body>
</html>
```